Simple and clean poster/flyer design needed for public speaker!

SIMPLE AND CLEAN DESIGN NEEDED FOR POSTER/FLYER

I AM a public speaker based in London (www.corvanlethby.com)
and I would like to have a custom-made flyer/poster
(preferably in adobe CS4 template format) that I con customize (just changing the text) for my various speeches, topics and locations

I am looking for something very simple and clean.
NO extravagance or crowded poster, but a rather beautiful clean and eye-catching design that clearly informs people what i am talking about, where and when.

Go to my website www.corvanlethby.com
to see the colour scheme and style that I like
my poster should be like the website, similar colours, logo, clean, simple and clear.

Summary

(1) simple and clean design
(2) design that fits my brand (see website)
(3) clear and eye-catching to promote my speeches
(4) customizable for my various talks, by simply chancing the text (Please Adobe Photoshop CS4 template format)
(5)in A3, A4, A5, A6 sizes, so i can use it for both flyers and small posters

ADDITIONS

BIG BOLD HEADLINE TO GRAP ATTENTION, greatest prominence

sub headline to explain, smaller than the headline, but still prominent on the poster

just a few bullet points to list the benefits and answer the “whats in for me”-question
this is for people who are already interested and continue reading, medium prominence.

WHERE, WHEN, HOW MUCH-information, in the lower section of the poster, little text, but clearly visible

only one point of CONTACT on my poster “www.corvanlethby.com”, bit big and clear so that it is very prominent

little text, effectively used
LESS IS MORE
Updates

contact me regarding logo files and any questions you may have!

for the logo files go to

https://share.dropvaultex.net/f/x.aspx?k=41c07d2e9ab35f18c6d2

click on the folder "logo pack" to see the files

thanks for your interest. hope to see great designs!
I am really looking forward to it
if you have any questions, please do not hesitate to ask

Kind Regards
Corvan
 

• Simple, clean design, text sparingly used.

• The mood should be light-hearted, calm, bright, simple and friendly, comic like

• a lot of white space, calling more attention to the content

• a light blue, dark blue, white and black colour scheme as seen on the homepage (www.corvanlethby.com) please use the exact same colours as seen on the homepage.

White being most predominant, 2 different blue used to highlight something, black for text on white background.

• One graphic would be cool, as long as it is blue. It could be waves-like graphic, or something like the white pattern in the background, in my case just in blue on white background > http://www.quillmereretreathouse.org/., I do not mean exactly this graphic and not that crowded but a simple single graphic in blue as long as it fits the theme and feel of my poster

Top o f the poster

• (a )One short bold headline (TALK TITLE) with a sub-headline below it (hook)

• or (b) headline as question (…....?) and below sub-headline offering the solution (my talk ;-) of course)

• 3 benefits as on homepage, that I can adapt for each talk (bottom right of my start site “what are you looking for?” either blue on white, or as in the page white on blue...whatever looks better and fits the design). Not sure how that looks, and if to include it!

• the bottom of the poster will have “Where”-information “when”-information “ticket price” info

• contact at the very bottom...for more into or to purchase tickets (my website and email)

If you have any questions or need clarification please write me!

Requirements
Must have
• lot of white space
• less is more - simple design
• little text, little graphics- only used when necessary to greatest effect.
• light, friendly, modern feel
• blue-color scheme

```html
<!DOCTYPE html>
<html lang="en">
<head>
<meta charset="utf-8">
<title>Talk Title – Corvan Lethby, Spiritual Speaker</title>
<link rel="stylesheet" href="https://fonts.googleapis.com/css2?family=Archivo:wght@400;800;900&display=swap">
<style>
  :root {
    --paper: #f1f1f1;
    --paper-light: #fbfbfb;
    --band: rgba(255, 255, 255, 0.75);
    --frame: #a9a9a9;
    --bubble-line: #9c9c9c;
    --bubble-fill: #ffffff;
    --blue-light: #cdeef5;
    --blue-title: #8ad8ea;
    --blue-mid: #35aacb;
    --blue-dark: #1f8fb2;
    --ink: #2a2a2a;
  }
  html, body {
    margin: 0;
    padding: 0;
    width: 847px;
    height: 1200px;
    overflow: hidden;
    background: var(--paper);
  }
  .poster {
    display: block;
    width: 847px;
    height: 1200px;
    font-family: "Archivo", Arial, sans-serif;
  }
  .brace {
    font-family: "Archivo", Arial, sans-serif;
    font-weight: 400;
    fill: var(--blue-mid);
  }
  .talk-title {
    font-weight: 900;
    font-size: 98px;
    fill: var(--blue-title);
    stroke: var(--blue-dark);
    stroke-width: 2.5px;
    paint-order: stroke;
  }
  .talk-hook {
    font-weight: 900;
    font-size: 52px;
    fill: var(--blue-mid);
  }
  .bubble-outline {
    fill: var(--bubble-fill);
    stroke: var(--bubble-line);
    stroke-width: 7px;
    stroke-linejoin: round;
  }
  .bubble-inner {
    fill: var(--blue-light);
  }
  .bubble-label {
    font-weight: 800;
    fill: var(--blue-mid);
    text-anchor: middle;
  }
  .speaker-mark {
    fill: var(--blue-mid);
  }
  .speaker-name {
    font-weight: 400;
    font-size: 34px;
    fill: var(--blue-mid);
    letter-spacing: 1px;
  }
  .speaker-role {
    font-weight: 400;
    font-size: 20px;
    fill: var(--ink);
    letter-spacing: 1px;
  }
</style>
</head>
<body>
<svg class="poster" viewBox="0 0 847 1200" xmlns="http://www.w3.org/2000/svg">
  <defs>
    <linearGradient id="paper-tone" x1="0" y1="0" x2="0" y2="1">
      <stop offset="0" stop-color="var(--paper)"/>
      <stop offset="0.5" stop-color="var(--paper-light)"/>
      <stop offset="1" stop-color="var(--paper)"/>
    </linearGradient>
  </defs>

  <!-- Background -->
  <rect class="backdrop" x="0" y="0" width="847" height="1200" fill="url(#paper-tone)" role="img" aria-label="Faint light grey damask pattern across the background"/>

  <!-- Light diagonal bands -->
  <g class="light-bands">
    <polygon points="160,270 847,190 847,300 160,390" fill="var(--band)"/>
    <polygon points="420,400 847,350 847,470 420,510" fill="var(--band)"/>
  </g>

  <!-- Frame -->
  <rect class="frame" x="28" y="26" width="791" height="1130" fill="none" stroke="var(--frame)" stroke-width="3"/>

  <!-- Headline block -->
  <g class="headline">
    <text class="brace" x="62" y="370" font-size="330">{</text>
    <text class="brace" x="680" y="420" font-size="330">}</text>
    <text class="talk-title" x="150" y="245" transform="rotate(-4 420 220)">Talk Title</text>
    <text class="talk-hook" x="215" y="330" transform="rotate(-4 420 310)">Insert hook here</text>
  </g>

  <!-- When bubble -->
  <g class="bubble bubble-when">
    <polygon class="bubble-outline" points="160,670 112,750 230,690"/>
    <ellipse class="bubble-outline" cx="264" cy="608" rx="197" ry="91"/>
    <polygon points="163,665 124,732 226,684" fill="var(--bubble-fill)"/>
    <ellipse class="bubble-inner" cx="270" cy="614" rx="150" ry="66"/>
    <text class="bubble-label" x="262" y="630" font-size="54">When?</text>
  </g>

  <!-- Where bubble -->
  <g class="bubble bubble-where">
    <polygon class="bubble-outline" points="660,600 720,563 700,620"/>
    <ellipse class="bubble-outline" cx="608" cy="679" rx="162" ry="101"/>
    <polygon points="664,605 710,577 696,620" fill="var(--bubble-fill)"/>
    <ellipse class="bubble-inner" cx="590" cy="688" rx="124" ry="62"/>
    <text class="bubble-label" x="600" y="700" font-size="42" transform="rotate(-8 600 690)">Where?</text>
  </g>

  <!-- Cost bubble -->
  <g class="bubble bubble-cost">
    <polygon class="bubble-outline" points="290,830 304,892 340,838"/>
    <ellipse class="bubble-outline" cx="345" cy="780" rx="91" ry="71"/>
    <polygon points="294,826 305,876 336,832" fill="var(--bubble-fill)"/>
    <ellipse class="bubble-inner" cx="342" cy="786" rx="72" ry="50"/>
    <text class="bubble-label" x="340" y="800" font-size="44">Cost</text>
  </g>

  <!-- Website bubble -->
  <g class="bubble bubble-web">
    <polygon class="bubble-outline" points="450,1080 416,1115 510,1090"/>
    <ellipse class="bubble-outline" cx="588" cy="1034" rx="203" ry="71"/>
    <polygon points="452,1076 428,1103 504,1085" fill="var(--bubble-fill)"/>
    <ellipse class="bubble-inner" cx="606" cy="1044" rx="172" ry="56"/>
    <text class="bubble-label" x="586" y="1052" font-size="27" transform="rotate(-5 586 1044)">www.corvanlethby.com</text>
  </g>

  <!-- Speaker name -->
  <g class="speaker">
    <circle class="speaker-mark" cx="88" cy="1120" r="34"/>
    <text class="speaker-name" x="136" y="1134">CORVAN LETHBY</text>
    <text class="speaker-role" x="138" y="1164">SPIRITUAL SPEAKER</text>
  </g>
</svg>
</body>
</html>
```